business card for a massage therapy practice named 'Meadow and Willow Massage Studio'

I really need a trendy, yet easy on the eyes business card to complement my logo. Ideally with some gold or rose gold foil work.

My uploaded file of the logo I have in horizontal but I have a vertical version as well. Another color that is used in the website is a blush pink here and there. I'd like to see some trendy tropical leaves in the design.

```html
<!DOCTYPE html>
<html lang="en">
<head>
<meta charset="utf-8">
<title>Meadow and Willow Massage Studio — Business Card</title>
<link href="https://fonts.googleapis.com/css2?family=Montserrat:wght@400;500;600&display=swap" rel="stylesheet">
<style>
  :root {
    --backdrop: #2b2b2b;
    --card: #111111;
    --gold: #c9a37c;
    --gold-light: #e3c6a4;
    --gold-dark: #8f6f50;
    --rule: #5a4a3c;
  }
  * { box-sizing: border-box; margin: 0; padding: 0; }
  html, body {
    width: 1200px;
    height: 986px;
    overflow: hidden;
    background: var(--backdrop);
    font-family: "Montserrat", sans-serif;
  }
  .canvas {
    position: relative;
    width: 1200px;
    height: 986px;
  }
  .card {
    position: absolute;
    width: 560px;
    height: 320px;
    background: var(--card);
    border-radius: 3px;
    box-shadow: 0 18px 40px rgba(0,0,0,0.45);
    overflow: hidden;
  }

  /* Front */
  .card-front { left: 70px; top: 110px; }
  .brand {
    position: absolute;
    left: 120px;
    top: 96px;
    display: flex;
    align-items: center;
    gap: 22px;
  }
  .pineapple-art {
    width: 64px;
    height: 118px;
    display: block;
  }
  .brand-name {
    color: var(--gold);
    font-weight: 500;
    line-height: 1.25;
  }
  .brand-name .line-main { display: block; font-size: 30px; letter-spacing: 0.5px; }
  .brand-name .line-sub { display: block; font-size: 15px; letter-spacing: 5px; text-transform: uppercase; margin-top: 4px; }
  .social-handle {
    position: absolute;
    left: 270px;
    top: 222px;
    color: var(--gold);
    font-size: 10px;
    font-weight: 500;
    letter-spacing: 3px;
    text-transform: uppercase;
  }

  /* Back */
  .card-back { left: 570px; top: 560px; }
  .holder {
    position: absolute;
    left: 60px;
    top: 122px;
    color: var(--gold);
  }
  .holder-name { font-size: 28px; font-weight: 600; letter-spacing: 0.3px; }
  .holder-licence {
    font-size: 11px;
    font-weight: 500;
    letter-spacing: 2.5px;
    text-align: right;
    margin-top: 2px;
  }
  .divider {
    position: absolute;
    left: 314px;
    top: 90px;
    width: 1px;
    height: 112px;
    background: var(--rule);
  }
  .contact {
    position: absolute;
    left: 336px;
    top: 94px;
    color: var(--gold-light);
    font-size: 13px;
    line-height: 1.5;
  }
  .contact .group + .group { margin-top: 6px; }
  .foil-edge {
    position: absolute;
    left: 0;
    bottom: 0;
    width: 100%;
    height: 6px;
    background: linear-gradient(90deg, var(--gold-dark), var(--gold-light) 50%, var(--gold-dark));
  }
</style>
</head>
<body>
<main class="canvas">

  <section class="card card-front" aria-label="Card front">
    <div class="brand">
      <svg class="pineapple-art" role="img" aria-label="Gold foil engraved pineapple illustration" viewBox="0 0 64 118">
        <defs>
          <linearGradient id="foil" x1="0" y1="0" x2="1" y2="1">
            <stop offset="0" stop-color="#e3c6a4"/>
            <stop offset="1" stop-color="#8f6f50"/>
          </linearGradient>
        </defs>
        <rect width="64" height="118" rx="6" fill="url(#foil)" opacity="0.85"/>
      </svg>
      <div class="brand-name">
        <span class="line-main">Meadow and Willow</span>
        <span class="line-sub">Massage Studio</span>
      </div>
    </div>
    <p class="social-handle">@meadowandwillow</p>
  </section>

  <section class="card card-back" aria-label="Card back">
    <div class="holder">
      <p class="holder-name">Daniela Moreno</p>
      <p class="holder-licence">LMT #40215</p>
    </div>
    <div class="divider"></div>
    <address class="contact" style="font-style: normal;">
      <div class="group">
        <p>2140 Fern Ave #210</p>
        <p>Riverton, CA 90210</p>
      </div>
      <div class="group">
        <p>(555) 214-7730</p>
        <p>info@meadowandwillow.com</p>
        <p>www.meadowandwillow.com</p>
      </div>
    </address>
    <div class="foil-edge"></div>
  </section>

</main>
</body>
</html>
```